Business Card Design Project

Hi!
Looking for a business card design for my acupuncture/remedial massage business using a logo I've just had designed through this site!
I'd like the following details included:
Logo (obviously)
My name - Miranda Pellowtane
Clinic details -Complementary and Traditional Chinese Medicine Haven
42 Brindlewood Road
Ashbury Vale 3187
03 9471 6820
Website - www.pellowtanewell.com.au
I have the logo design in two different colour combinations, one predominantly green, and the other in reverse colours. I was thinking that the green logo would take up one whole side of the business card, then we could include the reverse logo on the more detailed side. I'd like to see how that looks.
I also had the idea that the heart in the logo could be printed in metallic red (depending on cost). Not sure if that comes into play now or at the printers.
Thanks!

```html
<!DOCTYPE html>
<html lang="en">
<head>
<meta charset="utf-8">
<title>Pellowtane Well – Business Card</title>
<link rel="stylesheet" href="https://fonts.googleapis.com/css2?family=Ubuntu:wght@500;700&family=Roboto+Condensed:wght@400&display=swap">
<style>
  :root {
    --jade: #1bb686;
    --clinic-red: #d42a25;
    --paper: #ffffff;
    --edge: #d9d9d9;
  }
  * { margin: 0; padding: 0; box-sizing: border-box; }
  html, body {
    width: 1200px; height: 820px; overflow: hidden;
    background: var(--paper);
  }
  .canvas { position: relative; width: 1200px; height: 820px; }

  .card { position: absolute; top: 0; height: 331px; }

  /* Front side */
  .card-front {
    left: 0; width: 588px;
    background: var(--jade);
    display: flex; align-items: center; justify-content: center;
  }
  .brand-name {
    font-family: "Ubuntu", sans-serif;
    font-weight: 700;
    line-height: 1.02;
    letter-spacing: -0.5px;
  }
  .card-front .brand-name {
    color: var(--paper);
    font-size: 50px;
  }

  /* Back side */
  .card-back {
    left: 612px; width: 588px;
    background: var(--paper);
    border-left: 1px solid var(--edge);
    border-right: 1px solid var(--edge);
  }
  .band { position: absolute; left: -1px; right: -1px; height: 12px; background: var(--jade); }
  .band-top { top: 0; }
  .band-bottom { bottom: 0; }

  .card-back .brand {
    position: absolute; left: 32px; top: 126px; width: 210px;
  }
  .card-back .brand-name { color: var(--jade); font-size: 36px; }

  .divider {
    position: absolute; left: 253px; top: 38px;
    width: 1.5px; height: 255px; background: var(--clinic-red);
  }

  .clinic-title {
    position: absolute; right: 41px; top: 24px;
    text-align: right;
    font-family: "Ubuntu", sans-serif; font-weight: 700;
    font-size: 23px; line-height: 31px;
    color: var(--clinic-red);
  }
  .practitioner {
    position: absolute; right: 41px; top: 181px;
    font-family: "Ubuntu", sans-serif; font-weight: 700;
    font-size: 20px; color: var(--clinic-red);
  }
  .contact {
    position: absolute; right: 40px; top: 214px;
    list-style: none;
    font-family: "Roboto Condensed", sans-serif;
    font-size: 16.5px; color: var(--jade);
  }
  .contact li {
    display: flex; justify-content: flex-end; align-items: center;
    height: 23px;
  }
  .contact .icon { width: 14px; height: 14px; margin-left: 12px; flex: none; }
  .contact .icon-spacer { width: 14px; margin-left: 12px; }
</style>
</head>
<body>
<div class="canvas">

  <section class="card card-front">
    <div class="brand-name">Pellowtane<br>Well</div>
  </section>

  <section class="card card-back">
    <div class="band band-top"></div>

    <div class="brand"><div class="brand-name">Pellowtane<br>Well</div></div>

    <div class="divider"></div>

    <h1 class="clinic-title">Complementary &amp;<br>Traditional Chinese<br>Medicine Haven</h1>

    <p class="practitioner">Miranda Pellowtane</p>

    <ul class="contact">
      <li>42 Brindlewood Road
        <svg class="icon" viewBox="0 0 14 14" aria-hidden="true"><path d="M7 1a4.3 4.3 0 0 0-4.3 4.3C2.7 8.5 7 13.3 7 13.3s4.3-4.8 4.3-8A4.3 4.3 0 0 0 7 1z" fill="#d42a25"/><circle cx="7" cy="5.3" r="1.6" fill="#fff"/></svg>
      </li>
      <li>Ashbury Vale 3187<span class="icon-spacer"></span></li>
      <li>03 9471 6820
        <svg class="icon" viewBox="0 0 14 14" aria-hidden="true"><path d="M4 2.2 5.6 4.6 4.5 5.9c.7 1.6 2 2.9 3.6 3.6l1.3-1.1 2.4 1.6-.8 2C7.3 11.8 2.2 6.7 2 2.9z" fill="#d42a25"/><path d="M8.5 1.5a4 4 0 0 1 4 4M8.4 3.3a2.2 2.2 0 0 1 2.3 2.3" stroke="#d42a25" stroke-width="1" fill="none"/></svg>
      </li>
      <li>www.pellowtanewell.com.au
        <svg class="icon" viewBox="0 0 14 14" aria-hidden="true"><circle cx="7" cy="7" r="5.7" fill="#d42a25"/><g stroke="#fff" stroke-width="0.9" fill="none"><ellipse cx="7" cy="7" rx="2.4" ry="5.7"/><path d="M1.3 7h11.4M2.2 4.2h9.6M2.2 9.8h9.6"/></g></svg>
      </li>
    </ul>

    <div class="band band-bottom"></div>
  </section>

</div>
</body>
</html>
```